Food packaging label design

The product name Crisplets, a thin, crispy, and delicious biscuit/cookie made from simple, all natural ingredients. Its name comes from the fact that it looks and tastes a lot like a biscotti cookie, but thinly sliced and much crispier and more delicious than a biscotti. There are currently two flavors: Pure Harvest, and Maple Orchard.

I am looking for a fresh, eye catchy design to go on the label for a rice paper stand up pouch (pouch sample attached). Label size are as follows:

4 oz bag - Width X Height
top: 4.5" x 3.5" bottom: 4.5" x 1.5"

12 oz bag
top: 6.5" x 5.5" bottom: 6.5" x 1.5"

I would like for the top portion of the packaging to include:

Crisplets name
Tag line " a thinner, crispier, and more delicious cousin to the biscotti"
simple and natural ingredients

bottom to include:
net weight
ingredients: wheat flour, eggs, sugar, almonds

Attached is a copy of something I created in powerpoint. you can recreate this using graphic designer software per label specs and improve on it or supprise me with something totally awesome. The key is that it that the colors and design needs to pop or contrast against the white rice paper bag and design needs to be eye catchy, fun and whimsical.

Please refer to link below for best practices for creating artwork for labels to ensure correct format for printing.
http://www.printwellmark.example/label-articles/best-practices-designing-custom-labels/

Good luck!
Updates

Target Market(s)

educated, health conscious consumers such as customers who shops at green basket, brewhollow, market pennys

Industry/Entity Type

Graphic Designer

Requirements
Should not have
• busy or clutter design

```html
<!DOCTYPE html>
<html lang="en">
<head>
<meta charset="utf-8">
<title>Crisplets – Maple Orchard pouch label</title>
<link rel="stylesheet" href="https://fonts.googleapis.com/css2?family=Fira+Sans:ital,wght@0,800;0,900;1,800&family=Courgette&family=Roboto+Condensed:wght@400;700&display=swap">
<style>
  :root {
    --canvas: #ffffff;
    --ink: #111111;
    --label-red: #e2331d;
    --label-orange: #f68a1c;
    --label-glow: #ffcf3a;
    --band-blue: #2f3494;
    --brand-yellow: #ffe14d;
    --tag-maroon: #5b0f12;
    --strip-red: #e8391f;
    --strip-text: #fff3a8;
    --ingredient-ink: #3a0d0d;
    --biscuit-light: #f3e2bd;
    --biscuit-dark: #c99a5a;
  }
  * { box-sizing: border-box; margin: 0; padding: 0; }
  html, body { width: 1200px; height: 1000px; overflow: hidden; background: var(--canvas); }
  .canvas { position: relative; width: 1200px; height: 1000px; }

  .dimension-lines { position: absolute; inset: 0; }
  .dim-text {
    font-family: "Roboto Condensed", sans-serif;
    font-weight: 700;
    font-size: 24px;
    fill: var(--ink);
  }

  .label {
    position: absolute;
    left: 323px; top: 105px;
    width: 585px; height: 845px;
    overflow: hidden;
  }
  .label-top {
    position: absolute; left: 0; top: 0; width: 100%; height: 403px;
    background:
      radial-gradient(ellipse 60% 45% at 55% 30%, var(--label-glow) 0%, rgba(255,207,58,0) 70%),
      linear-gradient(180deg, var(--label-orange) 0%, #f79a22 55%, #f58a1d 100%),
      var(--label-red);
    box-shadow: inset 0 0 60px rgba(214,40,20,0.8);
  }
  .biscuit-art {
    position: absolute; left: 325px; top: 70px; width: 190px; height: 120px;
    border-radius: 10px;
    background: linear-gradient(135deg, var(--biscuit-light), var(--biscuit-dark));
    transform: rotate(-18deg);
  }
  .brand-name {
    position: absolute; left: 0; top: 120px; width: 100%;
    text-align: center;
    font-family: "Fira Sans", sans-serif;
    font-weight: 900;
    font-size: 104px;
    line-height: 1;
    color: var(--brand-yellow);
  }
  .tagline {
    position: absolute; left: 72px; top: 272px; width: 460px;
    font-family: "Fira Sans", sans-serif;
    font-weight: 800;
    font-size: 18px;
    line-height: 1.15;
    color: var(--tag-maroon);
    text-transform: uppercase;
    transform: rotate(3deg);
  }
  .tagline span { display: block; }
  .tagline span + span { padding-left: 96px; }
  .natural-strip {
    position: absolute; left: 120px; top: 374px; width: 345px; height: 28px;
    background: var(--strip-red);
    font-family: "Fira Sans", sans-serif;
    font-style: italic;
    font-weight: 800;
    font-size: 16px;
    line-height: 28px;
    color: var(--strip-text);
    text-align: center;
  }
  .flavour-band, .weight-band {
    position: absolute; left: 0; width: 100%;
    background: var(--band-blue);
    color: #ffffff;
    font-family: "Courgette", cursive;
    text-align: center;
  }
  .flavour-band { top: 403px; height: 52px; font-size: 27px; line-height: 52px; }
  .product-photo {
    position: absolute; left: 0; top: 455px; width: 100%; height: 195px;
    background: linear-gradient(160deg, #e9d3a6 0%, #f6e7c6 40%, #d9b47c 75%, #eedcb4 100%);
  }
  .weight-band { top: 650px; height: 38px; font-size: 21px; line-height: 38px; }
  .label-bottom {
    position: absolute; left: 0; top: 688px; width: 100%; height: 157px;
    background: linear-gradient(180deg, #f58a1d 0%, var(--label-orange) 40%, #ef5a1f 100%);
    box-shadow: inset 0 0 50px rgba(214,40,20,0.7);
    text-align: center;
    font-family: "Roboto Condensed", sans-serif;
    color: var(--ingredient-ink);
  }
  .ingredients-title { margin-top: 26px; font-weight: 700; font-size: 18px; }
  .ingredients-list { margin-top: 2px; font-size: 19px; }
</style>
</head>
<body>
<div class="canvas">
  <svg class="dimension-lines" width="1200" height="1000" viewBox="0 0 1200 1000" aria-hidden="true">
    <g stroke="#111" stroke-width="1.5" fill="none">
      <line x1="323" y1="48" x2="323" y2="90"/>
      <line x1="908" y1="48" x2="908" y2="90"/>
      <line x1="330" y1="73" x2="901" y2="73"/>
      <line x1="262" y1="105" x2="305" y2="105"/>
      <line x1="262" y1="560" x2="305" y2="560"/>
      <line x1="287" y1="112" x2="287" y2="553"/>
      <line x1="262" y1="755" x2="305" y2="755"/>
      <line x1="262" y1="950" x2="305" y2="950"/>
      <line x1="287" y1="762" x2="287" y2="943"/>
    </g>
    <g fill="#111">
      <polygon points="323,73 340,67 340,79"/>
      <polygon points="908,73 891,67 891,79"/>
      <polygon points="287,105 281,122 293,122"/>
      <polygon points="287,560 281,543 293,543"/>
      <polygon points="287,755 281,772 293,772"/>
      <polygon points="287,950 281,933 293,933"/>
    </g>
    <text class="dim-text" x="615" y="56" text-anchor="middle">4.5”</text>
    <text class="dim-text" transform="translate(270 332) rotate(-90)" text-anchor="middle">3.5”</text>
    <text class="dim-text" transform="translate(270 852) rotate(-90)" text-anchor="middle">1.5”</text>
  </svg>

  <div class="label">
    <section class="label-top">
      <div class="biscuit-art" role="img" aria-label="Illustration of two thin almond biscuit slices"></div>
      <h1 class="brand-name">Crisplets</h1>
      <p class="tagline"><span>A thinner, crispier, and more</span><span>delicious cousin to the biscotti</span></p>
      <p class="natural-strip">Simple and natural ingredients</p>
    </section>
    <h2 class="flavour-band">Maple Orchard</h2>
    <div class="product-photo" role="img" aria-label="Photo of thin sliced almond biscuits piled together"></div>
    <p class="weight-band">Net weight: 6 oz</p>
    <section class="label-bottom">
      <p class="ingredients-title">Ingredients:</p>
      <p class="ingredients-list">Wheat flour, eggs, sugar, almonds</p>
    </section>
  </div>
</div>
</body>
</html>
```